Business Card Design for Orthopaedic Surgeon

This is a double-sided glossy business card. I prefer baby blue, teal, and green as color schemes. I have my logo already (many colors that you can choose from). I have photos and examples of my old card (very bland but has the information in it). I also have one that my assistant tried to design, but the writing is too small and I don't love the formatting. But it is close!
I would like my logo to be on the business card but I'm uploading my logo in many different colors so you can choose which one looks best based on the color scheme. I also uploaded many sized headshots so you can choose the best resolution one.

Additional information:
Correct business address:
4382 NW 58th Lane, Suite 305
Tamarac, FL 33417

Everything else on both business cards are accurate.

I actually need 2 different business cards generated. One that includes my cell phone number-- Personal cell: 585-314-9062 in addition to Office phone: (954) 316-4870 and Office Fax: 954-316-4881. Again, one card would have my personal cell and one wouldn't

Overall I just think the baby blue card (uploaded) is missing something on the front--of course it is also missing my office phone/fax/personal cell. I do want my website on the front too. Email: info@wellsorthocare.example

You can use your discretion about what goes on the front vs. what goes on the back to eliminated clutter.

Oh and on the back, I would like to list "Conditions Treated" (not specialties include). The list is:
Carpal Tunnel
Trigger Finger
Ganglion Cysts
Hand Tumors
Han & Wrist Arthritis
Hand, Wrist & Elbow Tendonitis
Fractures of the Hand, Wrist, Elbow and Humerus
Nerve Injuries of the Hand, Wrist & Elbow
Microsurgery
Wrist Arthroscopy
Endoscopic Surgery

Target Market(s)

Primary care doctors, Lawyers, patients

Industry/Entity Type

Medical

Contact Information for Business Card

Please see above in project description

Colors

Designer to choose colors to be used in the design.

Requirements
Must have
• -Correct office info, Board Certified Orthopaedic Hand & Upper Extremity Surgeon
Nice to have
• Something that is classy and wow!

```html
<!DOCTYPE html>
<html lang="en">
<head>
<meta charset="utf-8">
<title>Wells Hand – Business Card</title>
<link href="https://fonts.googleapis.com/css2?family=Montserrat:wght@400;700&display=swap" rel="stylesheet">
<style>
  :root{
    --bg:#2b2b2b;
    --card:#111111;
    --green:#66c044;
    --text:#f2f2f2;
  }
  *{box-sizing:border-box;margin:0;padding:0}
  html,body{width:1200px;height:1059px;overflow:hidden;background:var(--bg)}
  body{position:relative;font-family:'Montserrat',sans-serif;color:var(--text)}
  .card{position:absolute;width:690px;height:392px;background:var(--card);border-radius:16px;overflow:hidden}
  .card--front{left:256px;top:88px}
  .card--back{left:254px;top:546px}
  .accent-band{position:absolute;left:0;bottom:0;width:100%;height:16px}
  .headshot{position:absolute;left:37px;top:32px;width:120px;height:176px;border:2px solid var(--green);
    background:linear-gradient(180deg,#8a8a8a 0%,#e6e6e6 35%,#3a3a3a 70%,#121212 100%)}
  .name{position:absolute;left:38px;top:236px;font-weight:700;font-size:26px;color:var(--green);letter-spacing:.3px}
  .title{position:absolute;left:38px;top:285px;font-size:17.5px;line-height:26px}
  .brand{position:absolute;display:flex;align-items:center;justify-content:center;border:4px solid var(--green);border-radius:50%}
  .brand span{font-weight:700;color:var(--green);text-align:center;line-height:1.15;letter-spacing:1px}
  .card--front .brand{left:385px;top:34px;width:150px;height:150px}
  .card--front .brand span{font-size:20px}
  .card--back .brand{left:512px;top:118px;width:158px;height:158px}
  .card--back .brand span{font-size:21px}
  .contact{position:absolute;left:384px;top:204px;list-style:none;font-size:17.5px}
  .contact li{display:flex;align-items:flex-start;height:26px}
  .contact li.address{height:52px}
  .contact svg{width:15px;height:15px;margin:4px 12px 0 0;flex:none;fill:var(--green)}
  .conditions{position:absolute;left:26px;top:50px;list-style:none;font-size:17.5px}
  .conditions li{height:26.2px;display:flex;align-items:center}
  .conditions li::before{content:"";width:7px;height:7px;border-radius:50%;background:var(--green);margin-right:6px;flex:none}
</style>
</head>
<body>

<section class="card card--front">
  <div class="headshot" role="img" aria-label="Portrait photo of the surgeon"></div>
  <h1 class="name">DANA WELLS, M.D</h1>
  <p class="title">Board Certified<br>Orthopaedic Hand &amp; Upper<br>Extremity Surgeon</p>

  <div class="brand"><span>WELLS<br>HAND</span></div>

  <ul class="contact">
    <li class="address">
      <svg viewBox="0 0 24 24"><path d="M12 2a7 7 0 0 0-7 7c0 5 7 13 7 13s7-8 7-13a7 7 0 0 0-7-7zm0 9.5A2.5 2.5 0 1 1 12 6.5a2.5 2.5 0 0 1 0 5z"/></svg>
      <span>4382 NW 58th Lane,<br>Suite 305 Tamarac, FL 33417</span>
    </li>
    <li>
      <svg viewBox="0 0 24 24"><path d="M6.6 10.8a15 15 0 0 0 6.6 6.6l2.2-2.2a1 1 0 0 1 1-.25 11.4 11.4 0 0 0 3.6.57 1 1 0 0 1 1 1V20a1 1 0 0 1-1 1A17 17 0 0 1 3 4a1 1 0 0 1 1-1h3.5a1 1 0 0 1 1 1c0 1.25.2 2.45.57 3.57a1 1 0 0 1-.25 1z"/></svg>
      <span>(954) 316-4870</span>
    </li>
    <li>
      <svg viewBox="0 0 24 24"><path d="M6 2h12v5H6zM4 8h16a2 2 0 0 1 2 2v6h-4v6H6v-6H2v-6a2 2 0 0 1 2-2zm4 8v4h8v-4z"/></svg>
      <span>954-316-4881</span>
    </li>
    <li>
      <svg viewBox="0 0 24 24"><path d="M2 5h20v14H2zm2 2v.5l8 5 8-5V7l-8 5z"/></svg>
      <span>info@wellsorthocare.example</span>
    </li>
    <li>
      <svg viewBox="0 0 24 24"><path d="M12 2a10 10 0 1 0 0 20 10 10 0 0 0 0-20zm-1 17.9A8 8 0 0 1 4 12l5 5v1a2 2 0 0 0 2 2zm6.9-2.5A2 2 0 0 0 16 16h-1v-3a1 1 0 0 0-1-1H8v-2h2a1 1 0 0 0 1-1V7h2a2 2 0 0 0 2-2v-.4a8 8 0 0 1 2.9 12.8z"/></svg>
      <span>www.wellsorthocare.example</span>
    </li>
  </ul>

  <svg class="accent-band" viewBox="0 0 690 16" preserveAspectRatio="none">
    <path d="M0 0H322L334 16H0Z" fill="var(--green)"/>
    <path d="M332 0H690V16H344Z" fill="var(--green)"/>
  </svg>
</section>

<section class="card card--back">
  <ul class="conditions">
    <li>Carpal Tunnel</li>
    <li>Trigger Finger</li>
    <li>Ganglion Cysts</li>
    <li>Hand Tumors</li>
    <li>Han &amp; Wrist Arthritis</li>
    <li>Hand, Wrist &amp; Elbow Tendonitis</li>
    <li>Fractures of the Hand, Wrist, Elbow and Humerus</li>
    <li>Nerve Injuries of the Hand, Wrist &amp; Elbow</li>
    <li>Microsurgery</li>
    <li>Wrist Arthroscopy</li>
    <li>Endoscopic Surgery</li>
  </ul>

  <div class="brand"><span>WELLS<br>HAND</span></div>

  <svg class="accent-band" viewBox="0 0 694 16" preserveAspectRatio="none">
    <path d="M0 0H326L338 16H0Z" fill="var(--green)"/>
    <path d="M336 0H694V16H348Z" fill="var(--green)"/>
  </svg>
</section>

</body>
</html>
```